Website design for HARBOR BOLTS. ( Lock company)

Harbor Bolts is a New York Based Company that manufactures a variety of high quality Locks which sell worldwide.

Our website: We need a 'face' on the Internet , a website that tells you who we are and what we do - 'An Identity'.

it is not an eCommerce website . the website is to show customers and potential distributers who we are and what we manufacture ( so they come away with a great impression of our company and our products) see www.quarrymillwheel.com

First glance impression: We are Professional; are locks are strong,and reliable. and we are ready to compete with other major Lock companies

Content: for starters the site will contain general information and background about our company (our story), were to buy our products, contact information, and display images of our Locks (and of course all the classic links including to all the legal and technical information). as time goes on we will add more features to the website i.e. Products, Videos blogs etc.

although at first there will not be that much content on the website - it should not look empty (it should be simple and clear but not empty) it should look and feel like a full fledged professional website (not a template)

Inspiration: here are a few sites which have the feel we are looking for:

General tone - quarrymillwheel.com bantrell.com (black is good - But not a must )

Simplicity, clarity - coolvantix.com hearthmate.com

the widescreen Image look - http://www.layoutgarden.com/demo/81952.html

we are considering perhaps having wide HQ images of Lion(s) in the background (but without the felling that it is a zoo or safari website) - it is not a must, its just an idea .

perhaps (if you find it looks good ) use a bit of that metal or chrome look to give it it a strong smooth feel (however it should not look like a dark prison)

We do not currently have a Logo ( if you feel you can design one that fits the above company description - we would love to see if it can work for us) We can talk about additional funds for the logo during this project.

Our working slogan is : Harbor Bolts - "Keeper of the Gate"

for your convenience we have attached a few images of the type of locks we sell

We are looking to collaborate with you throughout the project. We have ideas and visions we want implemented and we will help you along the way. So we can create the perfect website.

Thank you.

```html
<!DOCTYPE html>
<html lang="en">
<head>
<meta charset="utf-8">
<title>Harbor Bolts – Keeper of the Gate</title>
<link rel="stylesheet" href="https://fonts.googleapis.com/css2?family=Questrial&family=Open+Sans:wght@400;700&family=Arimo:wght@400&display=swap">
<style>
:root{
  --ink:#000;
  --navy:#0b1640;
  --glow:#1a2a70;
  --accent:#3d6ee0;
  --accent-soft:#5b86f0;
  --text:#c9c9c9;
  --muted:#8d8d8d;
  --nav-top:#ffffff;
  --nav-bottom:#c9c9c9;
  --nav-text:#333;
  --band:#1642b0;
  --band-dark:#0a1d5c;
  --footer:#141414;
}
*{margin:0;padding:0;box-sizing:border-box}
html,body{width:979px;height:1200px;overflow:hidden;background:var(--ink)}
.page{position:relative;width:979px;height:1200px;overflow:hidden;
  background:radial-gradient(ellipse 420px 260px at 490px 330px,#111c50 0%,#070b22 55%,#000 100%);
  font-family:"Open Sans",sans-serif;color:var(--text)}
.topbar{position:absolute;left:0;top:0;width:979px;height:46px;
  background:linear-gradient(var(--nav-top),#ededed 60%,var(--nav-bottom));border-bottom:1px solid #888}
.nav{position:absolute;left:111px;top:0;height:46px;display:flex;align-items:center;list-style:none;
  font-family:"Arimo",sans-serif;font-size:11.5px;text-transform:uppercase}
.nav li{padding:0 19px;border-left:1px solid #aaa;line-height:24px;color:var(--nav-text)}
.nav li:first-child{border-left:none}
.nav .current{color:#1f3d9c}
.social{position:absolute;top:10px;left:766px;display:flex;gap:3px}
.social span{width:26px;height:26px;border-radius:50%;background:radial-gradient(circle at 40% 35%,#6a6a6a,#2a2a2a);box-shadow:0 1px 2px #000}
.social span.active{background:radial-gradient(circle at 40% 35%,#4d72d8,#162c78)}
.brand{position:absolute;top:78px;left:0;width:979px;text-align:center}
.brand-name{font-family:"Questrial",sans-serif;font-size:38px;color:#4b6fd6;letter-spacing:1px;line-height:40px}
.brand-tag{font-family:"Questrial",sans-serif;font-size:14px;color:#fff;margin-left:90px}
.hero-art{position:absolute;left:240px;top:150px;width:425px;height:212px;border-radius:50%;
  background:radial-gradient(ellipse at 55% 50%,rgba(90,120,230,.55),rgba(40,60,160,.25) 55%,rgba(0,0,0,0) 75%)}
.headline{position:absolute;top:392px;left:0;width:979px;text-align:center;
  font-family:"Questrial",sans-serif;font-size:22px;color:#e8e8e8}
.showcase{position:absolute;left:0;top:562px;width:979px;height:131px;
  background:linear-gradient(#1c1c1e,#111 60%,#000);opacity:.9}
.arrow{position:absolute;top:534px;width:34px;height:34px;border-radius:50%;background:#2b2b2b}
.arrow svg{display:block}
.product{position:absolute;border-radius:10px}
.p1{left:150px;top:455px;width:95px;height:197px;background:linear-gradient(#bcbcbc 0 40%,#1c1c1c 40%)}
.p2{left:395px;top:446px;width:133px;height:202px;background:linear-gradient(#c9c9c9 0 45%,#9aa5b5 45% 88%,#2140a0 88%)}
.p3{left:639px;top:502px;width:185px;height:133px;background:radial-gradient(ellipse,#e8c27a,#a87a32 70%,rgba(0,0,0,0) 72%)}
.column{position:absolute;top:740px;width:200px}
.column h2{font-family:"Questrial",sans-serif;font-weight:400;font-size:19px;color:var(--accent-soft);margin-bottom:20px}
.column h2.upper{text-transform:uppercase}
.column p{font-size:10.5px;line-height:13.7px;margin-bottom:8px}
.col-who{left:128px}.col-what{left:393px}.col-contact{left:662px}
.divider{position:absolute;top:780px;width:1px;height:210px;background:linear-gradient(rgba(40,60,140,0),#1f2f70,rgba(40,60,140,0))}
.button{position:absolute;top:954px;width:103px;height:29px;background:linear-gradient(#fafafa,#c8c8c8);
  border-radius:2px;color:#222;font-family:"Arimo",sans-serif;font-size:11px;text-align:center;line-height:29px}
.contact-row{display:flex;align-items:flex-start;gap:8px;margin-top:12px;font-size:10.5px;line-height:15px}
.contact-row svg{flex:none;margin-top:1px}
.mark{position:absolute;left:662px;top:933px;width:190px;text-align:right}
.mark-name{font-family:"Questrial",sans-serif;font-size:31px;color:#777;line-height:34px}
.mark-tag{font-family:"Questrial",sans-serif;font-size:12px;color:#999}
.featured{position:absolute;left:128px;top:1021px;width:722px;height:101px;background:#061030;padding:4px}
.featured-inner{position:relative;width:100%;height:100%;background:linear-gradient(#1d4dc0,var(--band) 60%,#0e2f8a)}
.featured-title{position:absolute;left:0;top:0;width:185px;height:100%;
  background:linear-gradient(#1d4fc8,#1040b0);clip-path:polygon(0 0,160px 0,185px 50%,160px 100%,0 100%)}
.featured-title span{position:absolute;font-weight:700;font-size:25px;color:#fff;line-height:30px}
.featured-title .l1{left:14px;top:16px}.featured-title .l2{left:56px;top:48px}
.featured-chev{position:absolute;left:160px;top:0;width:42px;height:100%;background:var(--band-dark);
  clip-path:polygon(0 0,16px 0,42px 50%,16px 100%,0 100%,25px 50%)}
.thumb{position:absolute;top:11px;width:106px;height:69px;background:#fff}
.thumb i{position:absolute;inset:10px 25px;border-radius:6px}
.thumb .pad{background:linear-gradient(#d0d0d0 0 45%,#8fa0bb 45% 85%,#2546a8 85%)}
.thumb .knob{background:radial-gradient(ellipse,#e7c07a,#b38a40 70%,#fff 72%)}
.feat-arrow{position:absolute;top:40px}
.footer{position:absolute;left:0;top:1157px;width:979px;height:43px;background:var(--footer);border-top:1px solid #2a2a2a}
.footer-links{position:absolute;left:128px;top:15px;font-size:10.5px;color:#ccc}
.copyright{position:absolute;right:128px;top:15px;font-size:10.5px;color:#ccc}
.copyright b{font-weight:400;color:var(--accent)}
</style>
</head>
<body>
<div class="page">
  <header class="topbar">
    <ul class="nav">
      <li class="current">Home</li><li>Who We Are</li><li>What We Do</li><li>Our Products</li><li>Contact</li>
    </ul>
    <div class="social"><span></span><span class="active"></span><span></span></div>
  </header>

  <div class="brand">
    <div class="brand-name">Harbor Bolts</div>
    <div class="brand-tag">Keeper of the Gate</div>
  </div>

  <div class="hero-art" role="img" aria-label="Glowing blue big cat illustration"></div>
  <p class="headline">Lorem Ipsum is simply dummy text of the printing and typesetting industry.</p>

  <div class="showcase"></div>
  <div class="arrow" style="left:93px"><svg width="34" height="34"><path d="M20 10 L13 17 L20 24" stroke="#ddd" stroke-width="1.5" fill="none"/></svg></div>
  <div class="arrow" style="left:853px"><svg width="34" height="34"><path d="M14 10 L21 17 L14 24" stroke="#ddd" stroke-width="1.5" fill="none"/></svg></div>
  <div class="product p1" role="img" aria-label="Black combination key lock box"></div>
  <div class="product p2" role="img" aria-label="Laminated steel padlock with keys"></div>
  <div class="product p3" role="img" aria-label="Brass door knob lockset"></div>

  <section class="column col-who">
    <h2 class="upper">Who We Are</h2>
    <p>Lorem ipsum dolor sit amet, consectetur adipiscing elit.</p>
    <p>Aenean luctus, libero vitae tincidunt hen drerit, justo enim ultrices do lor, rutrum viverra dolor eros mattis leo. Ut tempor ipsum sed nisl ornare pharetra.</p>
    <p>Aenean luctus, libero vitae tincidunt hen drerit, justo enim ultrices do lor, rutrum viverra dolor eros mattis leo.</p>
  </section>
  <div class="divider" style="left:356px"></div>
  <section class="column col-what">
    <h2 class="upper">What We Do</h2>
    <p>Lorem ipsum dolor sit amet, consectetur adipiscing elit.</p>
    <p>Aenean luctus, libero vitae tincidunt hen drerit, justo enim ultrices do lor, rutrum viverra dolor eros mattis leo. Ut tempor ipsum sed nisl ornare pharetra.</p>
    <p>Aenean luctus, libero vitae tincidunt hen drerit, justo enim ultrices do lor, rutrum viverra dolor eros mattis leo.</p>
  </section>
  <div class="divider" style="left:625px"></div>
  <section class="column col-contact">
    <h2>Contact Us</h2>
    <p>Lorem ipsum dolor sit amet, consectetur adipiscing elit.</p>
    <div class="contact-row"><svg width="12" height="16" viewBox="0 0 12 16"><path d="M6 0a6 6 0 0 0-6 6c0 4 6 10 6 10s6-6 6-10a6 6 0 0 0-6-6zm0 8.5A2.5 2.5 0 1 1 6 3.5a2.5 2.5 0 0 1 0 5z" fill="#aaa"/></svg><span>218 Pier Street, Suite 310<br>Brooklyn, NY 11201</span></div>
    <div class="contact-row"><svg width="12" height="15" viewBox="0 0 12 15"><path d="M3 0 L5 4 L3.5 5.5 C4.5 8 6 10 8 11 L9.5 9.5 L12 12 L10 14.5 C5 14 1 8 1 2 Z" fill="#aaa"/></svg><span>718-555-0143</span></div>
    <div class="contact-row"><svg width="13" height="10" viewBox="0 0 13 10"><rect width="13" height="10" fill="#aaa"/><path d="M0 0 L6.5 5.5 L13 0" stroke="#000" fill="none"/></svg><span>info@harborbolts.com</span></div>
  </section>
  <div class="mark"><div class="mark-name">Harbor Bolts</div><div class="mark-tag">Keeper of the Gate</div></div>

  <div class="button" style="left:128px">Read More</div>
  <div class="button" style="left:394px">Read More</div>

  <section class="featured">
    <div class="featured-inner">
      <div class="featured-chev"></div>
      <div class="featured-title"><span class="l1">Featured</span><span class="l2">Products</span></div>
      <svg class="feat-arrow" style="left:213px" width="10" height="14"><path d="M8 1 L2 7 L8 13" stroke="#fff" stroke-width="2" fill="none"/></svg>
      <div class="thumb" style="left:233px"><i class="pad" role="img" aria-label="Padlock"></i></div>
      <div class="thumb" style="left:349px"><i class="knob" role="img" aria-label="Brass knob lockset"></i></div>
      <div class="thumb" style="left:465px"><i class="pad" role="img" aria-label="Padlock"></i></div>
      <div class="thumb" style="left:581px"><i class="knob" role="img" aria-label="Brass deadbolt"></i></div>
      <svg class="feat-arrow" style="left:695px" width="10" height="14"><path d="M2 1 L8 7 L2 13" stroke="#fff" stroke-width="2" fill="none"/></svg>
    </div>
  </section>

  <footer class="footer">
    <div class="footer-links">Home &nbsp;|&nbsp; Who We Are &nbsp;|&nbsp; What We Do &nbsp;|&nbsp; Our Products &nbsp;|&nbsp; Contact</div>
    <div class="copyright">Copyright © 2014, <b>HARBOR BOLTS.</b></div>
  </footer>
</div>
</body>
</html>
```